Poster for Office

Looking for an edgy, beautiful poster to hang up in my office that uses the quotes located below and potentially the image attached.

Title: Hadley's Maxims

Must have the following quotes included (punctuation and capitalization are flexible, do what you think looks the best they also don't need the quotation symbols):

"Don't order fish at a steakhouse"
"Be bold. The more you tell, the more you sell"
"admit nothing, deny everything, launch counterattack."
"avoid obviousness"
"never do anything until you're ready to do it"
"look good=feel good"
"always keep the advantage"
"never complain, never explain"
"Lay low, play dumb, keep moving"

Quotes

• Title: Hadley's Maxims

"avoid obviousness"
"look good=feel good"

```html
<!DOCTYPE html>
<html lang="en">
<head>
<meta charset="utf-8">
<title>Hadley's Maxims</title>
<link rel="stylesheet" href="https://fonts.googleapis.com/css2?family=Anton&family=Ubuntu:wght@700&display=swap">
<style>
  :root {
    --frame: #6e5220;
    --parchment-light: #f1d9a4;
    --parchment-mid: #e3b977;
    --parchment-dark: #c99a55;
    --figure-tone: #b98a4c;
    --ink: #111;
    --paper: #fff;
    --shadow: rgba(58, 36, 10, 0.85);
  }
  * { box-sizing: border-box; margin: 0; padding: 0; }
  html, body { width: 849px; height: 1200px; overflow: hidden; background: var(--frame); }
  .poster {
    position: relative;
    width: 849px;
    height: 1200px;
    background: var(--frame);
  }
  .artwork {
    position: absolute;
    left: 22px; top: 22px;
    width: 805px; height: 1156px;
    background:
      radial-gradient(ellipse 38% 30% at 78% 66%, rgba(185,138,76,0.45), transparent 70%),
      radial-gradient(ellipse 55% 45% at 45% 55%, rgba(185,138,76,0.35), transparent 75%),
      radial-gradient(ellipse 80% 70% at 40% 30%, var(--parchment-light), var(--parchment-mid) 60%, var(--parchment-dark));
  }
  .content {
    position: absolute;
    inset: 0;
  }
  .title {
    position: absolute;
    left: 93px; top: 52px;
    width: 662px;
    text-align: center;
    font-family: "Anton", "Arial Narrow", sans-serif;
    font-weight: 400;
    font-size: 100px;
    line-height: 1.2;
    text-transform: uppercase;
    color: var(--ink);
    -webkit-text-stroke: 2px var(--paper);
    paint-order: stroke fill;
    text-shadow: 0 0 1px var(--paper), 3px 3px 0 var(--paper), 4px 5px 6px var(--shadow);
    white-space: nowrap;
  }
  .title-rule {
    position: absolute;
    left: 93px; top: 186px;
    width: 660px; height: 6px;
    background: var(--ink);
  }
  .maxims {
    position: absolute;
    left: 92px; top: 242px;
    list-style: none;
    font-family: "Ubuntu", "Trebuchet MS", sans-serif;
    font-weight: 700;
    font-size: 34px;
    line-height: 43px;
    color: var(--paper);
    text-shadow: 2px 2px 1px var(--shadow), 0 0 3px rgba(58,36,10,0.6);
  }
  .maxim {
    position: relative;
    padding-left: 24px;
    margin-bottom: 41px;
  }
  .maxim::before {
    content: "•";
    position: absolute;
    left: 0;
  }
</style>
</head>
<body>
  <main class="poster">
    <div class="artwork" role="img" aria-label="Sepia portrait on aged parchment: a man seen from behind filling the sheet, with a smiling face at lower right"></div>
    <div class="content">
      <h1 class="title">Hadley's Maxims</h1>
      <div class="title-rule"></div>
      <ul class="maxims">
        <li class="maxim">Don't order fish at a steakhouse</li>
        <li class="maxim">Be bold. The more you tell,<br>the more you sell</li>
        <li class="maxim">Admit nothing, deny everything,<br>launch counterattack</li>
        <li class="maxim">Avoid obviousness</li>
        <li class="maxim">Never do anything until you're<br>ready to do it</li>
        <li class="maxim">Look good=Feel good</li>
        <li class="maxim">Always keep the advantage</li>
        <li class="maxim">Never complain, never explain</li>
        <li class="maxim">Lay low, play dumb, keep moving</li>
      </ul>
    </div>
  </main>
</body>
</html>
```